Business Card Design

I would like a logo created for the top left corner of the card please. I would like a checkerboard in a dark navy with the edges fading out and one random bright orange square.
Updates

I have attached some further notes and a really rough sketch of what I am after.  Thank you. :)

Target Market(s)

Construction, mining, mechanical

Industry/Entity Type

Business

Contact Information for Business Card

Korvane Works Pty Ltd, Glen Hadwick, P. 0418365072, F. 0736209158, E.glen@korvaneworks.com.au, PO Box 87 YARRAWONGA Q 4581, ABN 53209874611

Font styles to use
Sans Serif

Requirements
Must have
• Really Dark Navy
Really bright Orange

```html
<!DOCTYPE html>
<html lang="en">
<head>
<meta charset="utf-8">
<title>Mara Lindqvist business card design sample</title>
<link href="https://fonts.googleapis.com/css2?family=Questrial&family=Oswald:wght@300;400;500&family=PT+Sans&display=swap" rel="stylesheet">
<style>
  :root {
    --navy: #1e1a52;
    --orange: #f05223;
    --green: #4f8a23;
    --grey-check: #c9c9cb;
    --paper: #ffffff;
    --card-edge: #9a9a9a;
  }
  * { box-sizing: border-box; margin: 0; padding: 0; }
  html, body { width: 1200px; height: 961px; overflow: hidden; background: var(--paper); }
  .sheet { position: relative; width: 1200px; height: 961px; background: var(--paper); }
  .band { position: absolute; left: 0; width: 1200px; background: var(--green); }
  .band--top { top: 0; height: 6px; }
  .band--bottom { bottom: 0; height: 8px; }
  .sheet-title {
    position: absolute; top: 27px; left: 0; width: 1200px; text-align: center;
    font: 15px "PT Sans", sans-serif; color: #222;
  }
  .design-label {
    position: absolute; left: 182px;
    font: 400 15px "Oswald", sans-serif; color: #111; letter-spacing: 0.5px;
  }
  .design-label--a { top: 108px; }
  .design-label--b { top: 559px; }

  .card {
    position: absolute; left: 276px; width: 647px; height: 398px;
    background: var(--paper); border: 1px solid var(--card-edge);
    box-shadow: 1px 2px 4px rgba(0,0,0,0.35); overflow: hidden;
  }
  .card--a { top: 88px; font-family: "Questrial", sans-serif; }
  .card--b { top: 526px; font-family: "Oswald", sans-serif; font-weight: 300; }

  .mark-area {
    position: absolute; left: 0; top: 0; width: 238px;
    background:
      radial-gradient(ellipse 45% 30% at 48% 30%, rgba(240,82,35,0.22), rgba(240,82,35,0) 70%),
      linear-gradient(90deg, rgba(201,201,203,0.9), rgba(201,201,203,0.55) 70%, rgba(201,201,203,0));
    -webkit-mask-image: linear-gradient(180deg, #000 35%, transparent 100%);
            mask-image: linear-gradient(180deg, #000 35%, transparent 100%);
  }
  .card--a .mark-area { height: 340px; }
  .card--b .mark-area { height: 340px; }

  .company {
    position: absolute; color: var(--navy);
    text-transform: uppercase; white-space: nowrap;
  }
  .card--a .company { left: 334px; top: 22px; width: 260px; text-align: center; font-size: 31px; line-height: 44px; }
  .card--b .company { left: 250px; top: 36px; font-size: 38px; line-height: 56px; font-weight: 400; }

  .holder { position: absolute; text-transform: uppercase; white-space: nowrap; }
  .card--a .holder { left: 364px; top: 148px; width: 210px; text-align: center; }
  .card--b .holder { left: 401px; top: 196px; }
  .holder__name { color: var(--navy); font-size: 26px; line-height: 30px; }
  .holder__phone { color: var(--orange); font-size: 23px; line-height: 30px; }
  .card--b .holder__name { font-size: 28px; font-weight: 400; }
  .card--b .holder__phone { font-size: 24px; font-weight: 400; }

  .contact { position: absolute; left: 36px; list-style: none; color: var(--navy); text-transform: uppercase; white-space: nowrap; }
  .card--a .contact { top: 203px; font-size: 20px; line-height: 29px; }
  .card--b .contact { top: 199px; font-size: 23px; line-height: 29px; font-weight: 400; }
  .contact__key, .contact__abn { color: var(--orange); }

  .stripe { position: absolute; left: 0; }
  .card--a .stripe--navy { top: 354px; width: 100%; height: 12px; background: var(--navy); }
  .card--a .stripe--orange { top: 366px; width: 100%; height: 11px; background: var(--orange); }
  .card--b .stripe--navy { top: 354px; width: 324px; height: 23px; background: var(--navy); }
  .card--b .stripe--orange { top: 354px; left: 324px; width: 323px; height: 23px; background: var(--orange); }
</style>
</head>
<body>
<main class="sheet">
  <div class="band band--top"></div>
  <h1 class="sheet-title">Mara Lindqvist business card design Sample</h1>

  <p class="design-label design-label--a">DESIGN - A</p>
  <article class="card card--a">
    <div class="mark-area" role="img" aria-label="Brand symbol area: navy checkerboard fading at the edges with orange accent squares"></div>
    <p class="company">Korvane Works<br>Pty Ltd</p>
    <div class="holder">
      <p class="holder__name">Glen Hadwick</p>
      <p class="holder__phone">0418 365 072</p>
    </div>
    <ul class="contact">
      <li>PO Box 87 Yarrawonga Q 4581</li>
      <li><span class="contact__key">P.</span> 0418 365 072</li>
      <li><span class="contact__key">F.</span> 07 3620 9158</li>
      <li><span class="contact__key">E.</span> glen@korvaneworks.com.au</li>
      <li class="contact__abn">ABN 53 209 874 611</li>
    </ul>
    <div class="stripe stripe--navy"></div>
    <div class="stripe stripe--orange"></div>
  </article>

  <p class="design-label design-label--b">DESIGN - B</p>
  <article class="card card--b">
    <div class="mark-area" role="img" aria-label="Brand symbol area: grey checkerboard fading at the edges with an orange cross of squares"></div>
    <p class="company">Korvane Works Pty Ltd</p>
    <div class="holder">
      <p class="holder__name">Glen Hadwick</p>
      <p class="holder__phone">0418 365 072</p>
    </div>
    <ul class="contact">
      <li>PO Box 87 Yarrawonga Q 4581</li>
      <li><span class="contact__key">P.</span> 0418 365 072</li>
      <li><span class="contact__key">F.</span> 07 3620 9158</li>
      <li><span class="contact__key">E.</span> glen@korvaneworks.com.au</li>
      <li class="contact__abn">ABN 53 209 874 611</li>
    </ul>
    <div class="stripe stripe--navy"></div>
    <div class="stripe stripe--orange"></div>
  </article>

  <div class="band band--bottom"></div>
</main>
</body>
</html>
```